BRELM - Letterhead

Willowmere Institute of Letters and Crafts (BRELM) is a non-profit organization that operates two tuition-free public schools - BRELM Elementary for grades K to 5th and BRELM College Prep for grades 6-12.

We are looking for a letterhead primarily to be used on Google Docs and Microsoft Word. Attached are two versions of our logo. One with our name spelled out and one with the acronym.

For Letterhead, we would like 3 addresses listed:

BRELM HQ
41872 Hollow Brook Lane, Suite 308
Cedar Hollow, CA 95512

BRELM Elementary (K-5)
18460 Marsh Ridge Boulevard
Cedar Hollow, CA 95512

BRELM College Prep (6-12)
27314 Del Sol Terrace
Maple Crest Springs, CA 95518

Our Phone Number is (555) 418-7062
Our Fax Number is the same (555) 418-7062

Our website is www.brelmschools.org

Target Market(s)

Education

Industry/Entity Type

Education

Font styles to use
Sans Serif

Colors
0054AA
0677BA
7BADD7
CADEEF
E8F1F8

Requirements
Must have
• Logo, Address, Phone Number, Website.
Nice to have
• Modern and clean design.
Should not have
• Prefer that there is no bleed -- the letterhead will mostly be used in PDF format however sometimes it will be printed and our printers can not do a full bleed

```html
<!DOCTYPE html>
<html lang="en">
<head>
<meta charset="utf-8">
<title>BRELM Letterhead</title>
<link href="https://fonts.googleapis.com/css2?family=Montserrat:ital,wght@0,400;0,600;0,700;1,400&family=Roboto+Condensed:wght@400;700&display=swap" rel="stylesheet">
<style>
  :root {
    --backdrop: #4d4d4d;
    --paper: #ffffff;
    --ink: #3a3a3a;
    --navy: #23399a;
    --brand-blue: #2a44a0;
    --sky: #3f7fc6;
    --green: #4a9a3a;
    --orange: #e0602e;
    --red: #d4553a;
  }
  * { margin: 0; padding: 0; box-sizing: border-box; }
  html, body { width: 1200px; height: 1200px; overflow: hidden; }
  body { background: var(--backdrop); position: relative; font-family: "Montserrat", sans-serif; color: var(--ink); }
  .letterhead { position: absolute; left: 238px; top: 132px; width: 723px; height: 936px; background: var(--paper); }
  .brand { position: absolute; left: 55px; top: 100px; display: flex; align-items: center; gap: 10px; }
  .brand-mark { width: 22px; height: 22px; background: var(--brand-blue); }
  .brand-name { font-family: "Montserrat", sans-serif; font-weight: 700; font-size: 38px; color: var(--brand-blue); letter-spacing: 1px; line-height: 1; }
  .right { position: absolute; right: 109px; text-align: right; }
  .date { top: 220px; font-weight: 700; font-size: 12.5px; }
  .recipient { top: 269px; font-size: 12.5px; line-height: 18px; }
  .recipient .name { font-weight: 700; }
  .recipient .role { font-style: italic; }
  .body-copy { position: absolute; left: 110px; top: 351px; width: 504px; font-size: 12.4px; line-height: 21.6px; text-align: justify; }
  .body-copy p + p { margin-top: 14px; }
  .closing { top: 680px; font-size: 12.5px; }
  .signature { position: absolute; left: 503px; top: 706px; width: 96px; height: 34px; background: linear-gradient(90deg, #ececec, #dcdcdc); border-radius: 17px; }
  .signer { position: absolute; right: 119px; top: 744px; font-weight: 700; font-size: 12.5px; }
  .contact-bar { position: absolute; left: 0; top: 835px; width: 723px; height: 80px; }
  .contact { position: absolute; top: 870px; transform: translateX(-50%); text-align: center; font-family: "Roboto Condensed", sans-serif; font-size: 7.4px; line-height: 11.2px; white-space: nowrap; color: var(--ink); }
  .contact .label { font-weight: 700; font-size: 8px; }
  .hq .label { color: var(--navy); }
  .elem .label { color: var(--green); }
  .prep .label { color: var(--orange); }
  .phone .label { color: var(--sky); }
  .fax .label { color: var(--navy); }
  .web .label { color: var(--ink); }
</style>
</head>
<body>
<main class="letterhead">
  <div class="brand"><span class="brand-mark"></span><span class="brand-name">BRELM</span></div>

  <div class="right date">Date, 22 February 2022</div>
  <div class="right recipient">
    <div>To:</div>
    <div class="name">Jordan Avery</div>
    <div class="role">Chief Officer</div>
  </div>

  <div class="body-copy">
    <p>Lorem ipsum dolor sit amet, consectetur adipiscing elit. Duis auctor sem vel metus interdum porta. Duis consequat bibendum felis eget cursus. Nulla eget purus vehicula ipsum finibus egestas. Nullam ligula ipsum, mollis sed gravida vitae, maximus eu dolor. Morbi luctus sem a congue consectetur. uis consequat bibendum felis eget cursus.</p>
    <p>Orci varius natoque penatibus et magnis dis parturient montes, nascetur ridiculus mus. Vestibulum congue eros auctor, ullamcorper libero blandit, tempor tellus. Proin vitae tellus et nunc fringilla lacinia. Sed augue erat, facilisis laoreet velit a, convallis mattis nunc. Nunc sagittis ligula vitae sollicitudin sollicitudin. Ullamcorper libero blandit, tempor tellus. Proin vitae tellus et nunc fringilla lacinia.</p>
    <p>Nulla facilisi. Nulla quis odio vitae purus aliquam fermentum ut nec diam. Fusce sed velit ultrices, aliquam augue ut, sollicitudin orci.</p>
  </div>

  <div class="right closing">Kind Regards</div>
  <div class="signature" role="img" aria-label="Handwritten signature"></div>
  <div class="signer">Jordan Avery</div>

  <svg class="contact-bar" viewBox="0 0 723 80" aria-hidden="true">
    <defs>
      <linearGradient id="bar-gradient" x1="0" x2="1">
        <stop offset="0" stop-color="#f5ec1a"/>
        <stop offset="0.3" stop-color="#f0c51c"/>
        <stop offset="0.5" stop-color="#e6882a"/>
        <stop offset="0.7" stop-color="#dc6238"/>
        <stop offset="1" stop-color="#d4553a"/>
      </linearGradient>
    </defs>
    <rect x="51" y="11" width="622" height="6" rx="3" fill="url(#bar-gradient)"/>
    <g fill="#fff" stroke="#d4553a" stroke-width="2">
      <circle cx="97" cy="14" r="9.5"/>
      <circle cx="226.5" cy="14" r="9.5"/>
      <circle cx="356" cy="14" r="9.5"/>
      <circle cx="467" cy="14" r="9.5"/>
      <circle cx="556" cy="14" r="9.5"/>
      <circle cx="647" cy="14" r="9.5"/>
    </g>
    <path d="M97 19c-3-3.5-4-5-4-6.5a4 4 0 0 1 8 0c0 1.5-1 3-4 6.5z" fill="#23399a"/>
    <circle cx="97" cy="12.5" r="1.4" fill="#fff"/>
    <path d="M226.5 19c-3-3.5-4-5-4-6.5a4 4 0 0 1 8 0c0 1.5-1 3-4 6.5z" fill="#4a9a3a"/>
    <circle cx="226.5" cy="12.5" r="1.4" fill="#fff"/>
    <path d="M356 19c-3-3.5-4-5-4-6.5a4 4 0 0 1 8 0c0 1.5-1 3-4 6.5z" fill="#e0602e"/>
    <circle cx="356" cy="12.5" r="1.4" fill="#fff"/>
    <path d="M463.5 10.5l1.8-.8 1.3 2.3-1 1c.5 1.2 1.4 2.1 2.6 2.6l1-1 2.3 1.3-.8 1.8c-3.8.4-7.6-3.4-7.2-7.2z" fill="#3f7fc6"/>
    <rect x="552" y="11" width="8" height="7" rx="1" fill="#23399a"/>
    <rect x="554" y="9" width="4" height="2.5" fill="none" stroke="#23399a" stroke-width="1"/>
    <g fill="none" stroke="#333" stroke-width="0.9">
      <circle cx="647" cy="14" r="4.5"/>
      <ellipse cx="647" cy="14" rx="2" ry="4.5"/>
      <line x1="642.5" y1="14" x2="651.5" y2="14"/>
    </g>
  </svg>

  <div class="contact hq" style="left:97px"><div class="label">BRELM HQ</div>41872 Hollow Brook Lane, Suite 308<br>Cedar Hollow, CA 95512</div>
  <div class="contact elem" style="left:226px"><div class="label">BRELM Elementary (K-5)</div>18460 Marsh Ridge Boulevard<br>Cedar Hollow, CA 95512</div>
  <div class="contact prep" style="left:356px"><div class="label">BRELM College Prep (6-12)</div>27314 Del Sol Terrace<br>Maple Crest Springs, CA 95518</div>
  <div class="contact phone" style="left:467px"><div class="label">(555) 418-7062</div></div>
  <div class="contact fax" style="left:556px"><div class="label">(555) 418-7062</div></div>
  <div class="contact web" style="left:643px; top:868px"><div class="label">www.brelmschools.org</div></div>
</main>
</body>
</html>
```